Re-design / improvement of an existing site This is to re-design a site (home 2 pages provided below ...). Only the home is to designer, the other pages are there for the brief only. The site is a social network sharing activities (sport, dance, cinema, outings ...) with friends, a bit like gatherly, but more fun, less 'business'. It is necessary to remain in clear tones, the site must above all be playful and 'friendly', warm, light, easy to understand and navigate. This is not a site intended to 'sell', but a site on which users often connect (like Chatterbox, for example), many pages are consulted at each visit, the site should not be aggressive or heavy , boring. Only call to action should be clearly visible, easy to find. The design is existing, psd can be provided, but the graphical result is not satisfactory. It is therefore pure graphic work that is required. Ergonomics is not to question, but the designer can change the sizes and shapes of buttons, areas, menu, pictograms, etc ... Eventually, the organization of headings can be changed, if the designer wishes it. But not the body of the page. Just think that the site will be responsive if you modify arrangements (header) It is a work of general consistency, balance in colors and shapes, general readability of the page. It should not be 'clutter', it must be intuitive and readable for users not necessarily very used to surf the internet. There are no imposed colors, one must only be 'friendly', playful, so no colors very marked, stay in clear tones ... The focus is on the human, the human relations, the pleasure, friendliness. The final name to put in the header is 'Loopsy', there is no definitive logo for the moment. Target: individuals, 50% men / women, aged 35 to 60, rather single. It is a work of general coherence, of balance in the colors and the forms. There are no imposed colors, one must only be 'friendly', playful, so no colors very marked, stay in clear tones ... There is a 'post it' effect in the header, it is not is not taxed.
Target Market(s)
BtoC, mixed men / women, aged 35 to 60, globally single.
Number of Pages Required
1 page
Font styles to use
Requirements
Must have
- Fund imperatively clear. The 'Brint Kavo' area in the header is a pub banner, so leave it unchanged, or put another ad in the same format. The photos of people must be kept: They are deliberately of poor quality, because on the site, we have no control of these photos that are uploaded by members. You can however consider shading these photos, or any effect that is manageable in HTML / CSS. The principle of avatars must also be preserved, but you can use other avatars if you wish. Finally, words are in pink or blue (pseudo members). It must also be kept, it corresponds to the sex of the members (woman / man).
Nice to have
- It is a work of general coherence, of balance in the colors and the forms. There are no imposed colors, one must only be 'friendly', playful, so no colors very marked, stay in clear tones ... There is a 'post it' effect in the header, it is not is not taxed.
Should not have
- Attention, the target is 35, do not put a typo too small, it must be very legible.

```html
<!DOCTYPE html>
<html lang="fr">
<head>
<meta charset="utf-8">
<title>Loopsy – Reviens à la vie réelle</title>
<link rel="stylesheet" href="https://fonts.googleapis.com/css2?family=Montserrat:wght@400;600;700;800&family=Open+Sans:wght@400;600;700&display=swap">
<style>
:root{
  --sky:#56c8e6;
  --sky-dark:#3fb4d4;
  --footer:#4bb8d5;
  --lime:#c3da55;
  --lime-dark:#a9c53a;
  --ink:#2b2b2b;
  --muted:#9a9a9a;
  --line:#e3e3e3;
  --soft:#f7f7f7;
  --white:#ffffff;
  --social:#3b5a9a;
}
*{box-sizing:border-box;margin:0;padding:0}
html,body{width:1200px;height:2585px;overflow:hidden}
body{position:relative;background:var(--white);font-family:"Open Sans",Arial,sans-serif;color:var(--ink)}
.abs{position:absolute}
a{color:inherit;text-decoration:none}

/* top bar */
.brand{left:74px;top:16px}
.brand-name{font-family:"Montserrat",sans-serif;font-weight:800;font-size:30px;color:var(--sky);line-height:34px}
.topbar-label{left:330px;top:27px;font-size:13px;color:#444}
.select{left:515px;top:18px;width:117px;height:35px;border:1px solid #ddd;border-radius:3px;font-size:12px;color:#bbb;padding:9px 12px}
.select svg{position:absolute;right:10px;top:12px}
.search{left:651px;top:18px;width:232px;height:35px;border:1px solid #ddd;border-radius:3px;font-size:12px;color:#bbb;padding:9px 12px}
.search-btn{position:absolute;right:-1px;top:-1px;width:48px;height:35px;background:var(--lime);border-radius:0 3px 3px 0;display:flex;align-items:center;justify-content:center}
.top-icons{left:918px;top:24px;display:flex;gap:22px}
.badge{position:absolute;left:1015px;top:18px;width:14px;height:14px;border-radius:50%;background:var(--lime);color:#fff;font-size:9px;text-align:center;line-height:14px}
.profile{left:1052px;top:15px;width:72px;height:40px;background:var(--sky);border-radius:20px}
.profile .avatar{position:absolute;left:2px;top:2px;width:36px;height:36px;border-radius:50%;background:linear-gradient(135deg,#c98b63,#5a4a3a)}
.profile svg{position:absolute;right:10px;top:11px}

/* nav */
.nav{left:0;top:70px;width:1200px;height:41px;background:var(--sky);display:flex;padding-left:74px}
.nav a{display:flex;align-items:center;gap:8px;padding:0 20px;height:41px;color:#fff;font-family:"Montserrat",sans-serif;font-size:11px;font-weight:600;text-transform:uppercase;border-right:1px solid rgba(255,255,255,.35)}
.nav a.active{background:var(--sky-dark)}

/* ad band */
.ad{left:455px;top:118px;width:669px;height:88px;display:flex;align-items:center}
.ad-brand{font-family:"Montserrat",sans-serif;font-weight:800;font-size:13px;letter-spacing:1px;width:120px}
.ad-arrows{width:22px;display:flex;flex-direction:column;gap:14px;align-items:center}
.ad-card{width:82px;height:82px;border:1px solid var(--line);margin-left:6px;font-size:9px;text-align:center;padding-top:10px;line-height:12px}
.ad-card b{display:block;margin-top:4px;font-size:11px}
.ad-card .swatch{width:40px;height:22px;margin:4px auto 0;background:#8fa3b8}
.ad-item{width:62px;height:82px;border:1px solid var(--line);margin-left:12px;display:flex;align-items:center;justify-content:center}
.ad-item span{display:block;width:24px;height:66px;border-radius:3px}
.ad-mark{position:absolute;right:0;top:0;width:10px;height:10px;background:#4aa7e0}

/* hero */
.hero-photo{left:0;top:213px;width:1200px;height:572px;background:linear-gradient(115deg,#d7e6f0 0%,#c9a48a 30%,#9f6a55 45%,#6f86a8 60%,#e2e6ea 100%)}
.login{left:74px;top:288px;width:322px;height:427px;background:#fff;box-shadow:0 2px 10px rgba(0,0,0,.12)}
.field{position:absolute;left:23px;width:277px;height:47px;background:#f1f1f1;font-size:14px;color:#555;padding:14px 16px}
.field svg{position:absolute;right:14px;top:15px}
.login-btn{position:absolute;left:23px;top:264px;width:277px;height:47px;background:var(--lime);color:#fff;font-family:"Montserrat",sans-serif;font-weight:700;font-size:13px;text-align:center;line-height:47px}
.forgot{position:absolute;left:0;width:322px;top:323px;text-align:center;font-size:11px;font-weight:600;text-decoration:underline}
.social-btn{position:absolute;left:46px;top:363px;width:231px;height:32px;background:var(--social);color:#fff;font-size:11px;line-height:32px;padding-left:60px}
.social-btn i{position:absolute;left:10px;top:9px;width:14px;height:14px;background:#fff}
.reasons{left:676px;top:213px;width:448px;height:572px;background:var(--lime);padding:40px 0 0 28px;color:#fff}
.reasons h2{font-family:"Montserrat",sans-serif;font-weight:800;font-size:28px;letter-spacing:.5px;margin-bottom:22px}
.reason{display:flex;gap:14px;height:111px}
.reason .num{flex:none;width:60px;height:60px;border:3px solid #fff;border-radius:50%;font-family:"Montserrat",sans-serif;font-weight:700;font-size:26px;text-align:center;line-height:54px}
.reason h3{font-family:"Montserrat",sans-serif;font-weight:700;font-size:18px;margin-bottom:4px}
.reason p{font-size:12px;font-weight:600;line-height:16px;width:280px}

/* cards */
.card{background:#fff;border:1px solid var(--line);box-shadow:0 1px 3px rgba(0,0,0,.06)}
.card-head{display:flex;justify-content:space-between;align-items:center;height:60px;margin:0 20px;border-bottom:1px solid var(--line)}
.card-head h2{font-family:"Montserrat",sans-serif;font-weight:600;font-size:18px}
.card-head a{font-size:12px;color:var(--lime-dark);font-weight:600}
.people{left:74px;top:842px;width:406px;height:649px}
.person{position:absolute;left:20px;width:366px;height:42px}
.person .pic{position:absolute;left:0;top:0;width:41px;height:41px}
.person .name{position:absolute;left:55px;top:3px;font-size:13px;font-weight:700}
.person .common{position:absolute;left:55px;top:22px;font-size:10px;color:var(--muted)}
.person .dismiss{position:absolute;left:305px;top:14px}
.person .add{position:absolute;right:0;top:6px;width:36px;height:28px;background:var(--sky);color:#fff;font-size:12px;font-weight:600;text-align:center;line-height:28px;border-radius:2px}
.events{left:526px;top:842px;width:598px;height:649px}
.event{position:absolute;left:18px;width:562px;height:44px}
.date{position:absolute;left:0;top:0;width:40px;height:44px;background:var(--lime);color:#fff;text-align:center;font-family:"Montserrat",sans-serif;font-weight:700;font-size:17px;line-height:22px}
.date small{display:block;font-size:10px;line-height:12px}
.ev-icon{position:absolute;left:51px;top:2px;width:40px;height:40px;border:1px solid var(--line);display:flex;align-items:center;justify-content:center}
.ev-title{position:absolute;left:104px;top:4px;font-size:13px;font-weight:600}
.ev-by{position:absolute;left:104px;top:24px;font-size:10px;color:var(--muted)}
.ev-by b,.ev-meta b{color:var(--lime-dark);font-weight:600}
.ev-meta{position:absolute;left:286px;top:24px;font-size:10px;color:var(--muted)}
.timeleft{position:absolute;right:0;top:0;width:130px;height:44px;border:1px solid var(--line);font-size:10px;text-align:right;padding:5px 10px 0 0;color:var(--muted)}
.timeleft span{display:block;margin-top:6px;color:var(--sky-dark);text-align:center;padding-left:8px}

/* what you can do */
.features{left:0;top:1562px;width:1200px;height:526px;background:var(--soft)}
.features h2{position:absolute;top:95px;width:1200px;text-align:center;font-family:"Montserrat",sans-serif;font-weight:400;font-size:32px;letter-spacing:.5px}
.feature{position:absolute;top:200px;width:230px;text-align:center}
.feature .circle{width:116px;height:116px;border-radius:50%;background:var(--lime);margin:0 auto;display:flex;align-items:center;justify-content:center}
.feature h3{margin-top:32px;font-family:"Montserrat",sans-serif;font-weight:700;font-size:17px;letter-spacing:1.5px}
.feature p{margin-top:14px;font-size:12px;line-height:21px;color:var(--muted)}

/* footer */
.footer{left:0;top:2088px;width:1200px;height:295px;background:var(--footer);color:#fff}
.col{position:absolute;top:68px}
.col h4{font-family:"Montserrat",sans-serif;font-size:11px;font-weight:700;letter-spacing:2px;margin-bottom:20px}
.col li{list-style:none;font-size:13px;height:33px}
.socials{position:absolute;left:860px;top:72px;display:flex;gap:14px}
.socials span{display:flex;align-items:center;gap:5px;font-size:11px;font-weight:600}
.socials span i{width:12px;height:12px;border-radius:50%;background:#fff}
.about-brand{left:74px;top:2454px}
.about{left:348px;top:2414px;width:592px}
.about h4{font-family:"Montserrat",sans-serif;font-size:11px;font-weight:700;letter-spacing:2px;margin-bottom:14px}
.about p{font-size:12.5px;line-height:24px;color:#333}
.ask{left:976px;top:2455px;width:148px;height:42px;border:3px solid var(--sky-dark);border-radius:21px;font-family:"Montserrat",sans-serif;font-weight:700;font-size:11px;letter-spacing:1.5px;text-align:center;line-height:36px}
</style>
</head>
<body>

<header>
  <div class="abs brand"><div class="brand-name">Loopsy</div></div>
  <div class="abs topbar-label">Ves les sorties et les membres</div>
  <div class="abs select">100<svg width="12" height="8" viewBox="0 0 12 8"><path d="M1 1l5 5 5-5" stroke="#aaa" stroke-width="2" fill="none"/></svg></div>
  <div class="abs search">search<span class="search-btn"><svg width="16" height="16" viewBox="0 0 16 16"><circle cx="6.5" cy="6.5" r="5" stroke="#fff" stroke-width="2" fill="none"/><path d="M10 10l5 5" stroke="#fff" stroke-width="2"/></svg></span></div>
  <div class="abs top-icons">
    <svg width="16" height="16" viewBox="0 0 16 16"><circle cx="8" cy="5" r="4" fill="#56c8e6"/><path d="M1 16c0-5 14-5 14 0z" fill="#56c8e6"/></svg>
    <svg width="18" height="16" viewBox="0 0 18 16"><circle cx="6" cy="5" r="3.5" fill="#56c8e6"/><circle cx="12" cy="5" r="3.5" fill="#56c8e6"/><path d="M0 16c0-5 18-5 18 0z" fill="#56c8e6"/></svg>
    <svg width="18" height="16" viewBox="0 0 18 16"><rect x="0" y="1" width="16" height="11" rx="2" fill="#56c8e6"/><path d="M4 12v4l4-4z" fill="#56c8e6"/></svg>
  </div>
  <div class="badge">3</div>
  <div class="abs profile"><span class="avatar" role="img" aria-label="Member profile photo"></span><svg width="18" height="18" viewBox="0 0 18 18"><circle cx="9" cy="9" r="6" stroke="#fff" stroke-width="3" stroke-dasharray="3 2" fill="none"/><circle cx="9" cy="9" r="3" fill="#fff"/></svg></div>
</header>

<nav class="abs nav">
  <a class="active" href="#">▣ Les sorties</a>
  <a href="#">▤ A faire / A voir</a>
  <a href="#">● Les membres</a>
  <a href="#">● Mes amis</a>
  <a href="#">▦ Mon planning</a>
  <a href="#">▬ Forum</a>
  <a href="#">◎ Groupes</a>
</nav>

<aside class="abs ad">
  <div class="ad-brand">BRINT KAVO</div>
  <div class="ad-arrows"><svg width="10" height="8"><path d="M0 8L5 0l5 8z" fill="#222"/></svg><svg width="10" height="8"><path d="M0 0l5 8 5-8z" fill="#222"/></svg></div>
  <div class="ad-card">Brint Kavo<br>Shorts<b>59,97 €</b><div class="swatch" role="img" aria-label="Shorts product photo"></div></div>
  <div class="ad-item"><span role="img" aria-label="Grey trousers product photo" style="background:#b9b6ad"></span></div>
  <div class="ad-item"><span role="img" aria-label="Dark jeans product photo" style="background:#2e3442"></span></div>
  <div class="ad-item"><span role="img" aria-label="Denim shorts product photo" style="background:#4f6f94;height:44px"></span></div>
  <div class="ad-item"><span role="img" aria-label="Navy jeans product photo" style="background:#2a3a5a"></span></div>
  <div class="ad-item"><span role="img" aria-label="Blue jeans product photo" style="background:#3f5878"></span></div>
  <div class="ad-item"><span role="img" aria-label="Brown trousers product photo" style="background:#5a3a30"></span></div>
  <i class="ad-mark"></i>
</aside>

<section>
  <div class="abs hero-photo" role="img" aria-label="Photo of a smiling couple sitting together outdoors on a bright day"></div>
  <form class="abs login">
    <div class="field" style="top:35px">First Name<svg width="16" height="16" viewBox="0 0 16 16"><circle cx="8" cy="5" r="3.5" stroke="#e8a0a0" fill="none"/><path d="M2 15c0-5 12-5 12 0z" stroke="#e8a0a0" fill="none"/></svg></div>
    <div class="field" style="top:90px">Last Name<svg width="16" height="16" viewBox="0 0 16 16"><circle cx="8" cy="5" r="3.5" stroke="#bbb" fill="none"/><path d="M2 15c0-5 12-5 12 0z" stroke="#bbb" fill="none"/></svg></div>
    <div class="field" style="top:144px">Email Address<svg width="18" height="14" viewBox="0 0 18 14"><rect x=".5" y=".5" width="17" height="13" stroke="#bbb" fill="none"/><path d="M1 1l8 7 8-7" stroke="#bbb" fill="none"/></svg></div>
    <div class="field" style="top:199px">••••••••••••<svg width="14" height="16" viewBox="0 0 14 16"><rect x=".5" y="7" width="13" height="8.5" stroke="#bbb" fill="none"/><path d="M3 7V4a4 4 0 018 0v3" stroke="#bbb" fill="none"/></svg></div>
    <div class="login-btn">LOGIN</div>
    <a class="forgot" href="#">Forgot your password?</a>
    <div class="social-btn"><i></i>Connexion Chatterbox</div>
  </form>
  <div class="abs reasons">
    <h2>4 BONNES RAISONS</h2>
    <div class="reason"><div class="num">1</div><div><h3>Partager, rire</h3><p>Plus jamais d'ennui les soirs et weekend! Participez a des milliers de sorties autour de chezvous, dans une ambiance conviviale et bienveillante</p></div></div>
    <div class="reason"><div class="num">2</div><div><h3>Partager, rire</h3><p>Plus jamais d'ennui les soirs et weekend! Participez a des milliers de sorties autour de chezvous, dans une ambiance conviviale et bienveillante</p></div></div>
    <div class="reason"><div class="num">3</div><div><h3>Partager, rire</h3><p>Plus jamais d'ennui les soirs et weekend! Participez a des milliers de sorties autour de chezvous, dans une ambiance conviviale et bienveillante</p></div></div>
    <div class="reason"><div class="num">4</div><div><h3>Partager, rire</h3><p>Plus jamais d'ennui les soirs et weekend! Participez a des milliers de sorties autour de chezvous, dans une ambiance conviviale et bienveillante</p></div></div>
  </div>
</section>

<section>
  <div class="abs card people">
    <div class="card-head"><h2>You may know</h2><a href="#">View all</a></div>
    <div class="person" style="top:82px"><span class="pic" role="img" aria-label="Member photo" style="background:#d8a46a"></span><span class="name">Claire Dubois</span><span class="common">14 people in common</span><svg class="dismiss" width="12" height="12"><circle cx="6" cy="6" r="6" fill="#ccc"/><path d="M4 4l4 4M8 4l-4 4" stroke="#fff" stroke-width="1.5"/></svg><span class="add">Add</span></div>
    <div class="person" style="top:138px"><span class="pic" role="img" aria-label="Member photo" style="background:#6e6a66"></span><span class="name">Marc Lenoir</span><span class="common">6 people in common</span><svg class="dismiss" width="12" height="12"><circle cx="6" cy="6" r="6" fill="#ccc"/><path d="M4 4l4 4M8 4l-4 4" stroke="#fff" stroke-width="1.5"/></svg><span class="add">Add</span></div>
    <div class="person" style="top:194px"><span class="pic" role="img" aria-label="Member photo" style="background:#5a4434"></span><span class="name">Samuel Okafor</span><span class="common">7 people in common</span><svg class="dismiss" width="12" height="12"><circle cx="6" cy="6" r="6" fill="#ccc"/><path d="M4 4l4 4M8 4l-4 4" stroke="#fff" stroke-width="1.5"/></svg><span class="add">Add</span></div>
    <div class="person" style="top:250px"><span class="pic" role="img" aria-label="Member photo" style="background:#d8a46a"></span><span class="name">Claire Dubois</span><span class="common">14 people in common</span><svg class="dismiss" width="12" height="12"><circle cx="6" cy="6" r="6" fill="#ccc"/><path d="M4 4l4 4M8 4l-4 4" stroke="#fff" stroke-width="1.5"/></svg><span class="add">Add</span></div>
    <div class="person" style="top:306px"><span class="pic" role="img" aria-label="Member photo" style="background:#6e6a66"></span><span class="name">Marc Lenoir</span><span class="common">6 people in common</span><svg class="dismiss" width="12" height="12"><circle cx="6" cy="6" r="6" fill="#ccc"/><path d="M4 4l4 4M8 4l-4 4" stroke="#fff" stroke-width="1.5"/></svg><span class="add">Add</span></div>
    <div class="person" style="top:362px"><span class="pic" role="img" aria-label="Member photo" style="background:#5a4434"></span><span class="name">Samuel Okafor</span><span class="common">7 people in common</span><svg class="dismiss" width="12" height="12"><circle cx="6" cy="6" r="6" fill="#ccc"/><path d="M4 4l4 4M8 4l-4 4" stroke="#fff" stroke-width="1.5"/></svg><span class="add">Add</span></div>
    <div class="person" style="top:418px"><span class="pic" role="img" aria-label="Member photo" style="background:#d8a46a"></span><span class="name">Claire Dubois</span><span class="common">14 people in common</span><svg class="dismiss" width="12" height="12"><circle cx="6" cy="6" r="6" fill="#ccc"/><path d="M4 4l4 4M8 4l-4 4" stroke="#fff" stroke-width="1.5"/></svg><span class="add">Add</span></div>
    <div class="person" style="top:474px"><span class="pic" role="img" aria-label="Member photo" style="background:#6e6a66"></span><span class="name">Marc Lenoir</span><span class="common">6 people in common</span><svg class="dismiss" width="12" height="12"><circle cx="6" cy="6" r="6" fill="#ccc"/><path d="M4 4l4 4M8 4l-4 4" stroke="#fff" stroke-width="1.5"/></svg><span class="add">Add</span></div>
    <div class="person" style="top:530px"><span class="pic" role="img" aria-label="Member photo" style="background:#5a4434"></span><span class="name">Samuel Okafor</span><span class="common">7 people in common</span><svg class="dismiss" width="12" height="12"><circle cx="6" cy="6" r="6" fill="#ccc"/><path d="M4 4l4 4M8 4l-4 4" stroke="#fff" stroke-width="1.5"/></svg><span class="add">Add</span></div>
    <div class="person" style="top:586px"><span class="pic" role="img" aria-label="Member photo" style="background:#5a4434"></span><span class="name">Samuel Okafor</span><span class="common">7 people in common</span><svg class="dismiss" width="12" height="12"><circle cx="6" cy="6" r="6" fill="#ccc"/><path d="M4 4l4 4M8 4l-4 4" stroke="#fff" stroke-width="1.5"/></svg><span class="add">Add</span></div>
  </div>

  <div class="abs card events">
    <div class="card-head"><h2>Latest Events</h2><a href="#">View all</a></div>
    <div class="event" style="top:80px"><div class="date">20<small>NOV</small></div><div class="ev-icon"><svg width="22" height="22" viewBox="0 0 22 22"><path d="M2 20L11 3l9 17z" fill="#56c8e6"/></svg></div><div class="ev-title">Hiking to Mount Elizabeth</div><div class="ev-by">by <b>Laurentie</b></div><div class="ev-meta"><b>1</b> participant(s) &nbsp;|&nbsp; <b>1</b> amis</div><div class="timeleft">time left<span>19 Hours 50 Minutes</span></div></div>
    <div class="event" style="top:136px"><div class="date">20<small>NOV</small></div><div class="ev-icon"><svg width="22" height="22" viewBox="0 0 22 22"><path d="M2 20L11 3l9 17z" fill="#56c8e6"/></svg></div><div class="ev-title">Hiking to Mount Elizabeth</div><div class="ev-by">by <b>Laurentie</b></div><div class="ev-meta"><b>1</b> participant(s) &nbsp;|&nbsp; <b>1</b> amis</div><div class="timeleft">time left<span>19 Hours 50 Minutes</span></div></div>
    <div class="event" style="top:192px"><div class="date">20<small>NOV</small></div><div class="ev-icon"><svg width="22" height="22" viewBox="0 0 22 22"><path d="M2 20L11 3l9 17z" fill="#56c8e6"/></svg></div><div class="ev-title">Hiking to Mount Elizabeth</div><div class="ev-by">by <b>Laurentie</b></div><div class="ev-meta"><b>1</b> participant(s) &nbsp;|&nbsp; <b>1</b> amis</div><div class="timeleft">time left<span>19 Hours 50 Minutes</span></div></div>
    <div class="event" style="top:248px"><div class="date">20<small>NOV</small></div><div class="ev-icon"><svg width="22" height="22" viewBox="0 0 22 22"><path d="M2 20L11 3l9 17z" fill="#56c8e6"/></svg></div><div class="ev-title">Hiking to Mount Elizabeth</div><div class="ev-by">by <b>Laurentie</b></div><div class="ev-meta"><b>1</b> participant(s) &nbsp;|&nbsp; <b>1</b> amis</div><div class="timeleft">time left<span>19 Hours 50 Minutes</span></div></div>
    <div class="event" style="top:304px"><div class="date">20<small>NOV</small></div><div class="ev-icon"><svg width="22" height="22" viewBox="0 0 22 22"><path d="M2 20L11 3l9 17z" fill="#56c8e6"/></svg></div><div class="ev-title">Hiking to Mount Elizabeth</div><div class="ev-by">by <b>Laurentie</b></div><div class="ev-meta"><b>1</b> participant(s) &nbsp;|&nbsp; <b>1</b> amis</div><div class="timeleft">time left<span>19 Hours 50 Minutes</span></div></div>
    <div class="event" style="top:360px"><div class="date">20<small>NOV</small></div><div class="ev-icon"><svg width="22" height="22" viewBox="0 0 22 22"><path d="M2 20L11 3l9 17z" fill="#56c8e6"/></svg></div><div class="ev-title">Hiking to Mount Elizabeth</div><div class="ev-by">by <b>Laurentie</b></div><div class="ev-meta"><b>1</b> participant(s) &nbsp;|&nbsp; <b>1</b> amis</div><div class="timeleft">time left<span>19 Hours 50 Minutes</span></div></div>
    <div class="event" style="top:416px"><div class="date">20<small>NOV</small></div><div class="ev-icon"><svg width="22" height="22" viewBox="0 0 22 22"><path d="M2 20L11 3l9 17z" fill="#56c8e6"/></svg></div><div class="ev-title">Hiking to Mount Elizabeth</div><div class="ev-by">by <b>Laurentie</b></div><div class="ev-meta"><b>1</b> participant(s) &nbsp;|&nbsp; <b>1</b> amis</div><div class="timeleft">time left<span>19 Hours 50 Minutes</span></div></div>
    <div class="event" style="top:472px"><div class="date">20<small>NOV</small></div><div class="ev-icon"><svg width="22" height="22" viewBox="0 0 22 22"><path d="M2 20L11 3l9 17z" fill="#56c8e6"/></svg></div><div class="ev-title">Hiking to Mount Elizabeth</div><div class="ev-by">by <b>Laurentie</b></div><div class="ev-meta"><b>1</b> participant(s) &nbsp;|&nbsp; <b>1</b> amis</div><div class="timeleft">time left<span>19 Hours 50 Minutes</span></div></div>
    <div class="event" style="top:528px"><div class="date">20<small>NOV</small></div><div class="ev-icon"><svg width="22" height="22" viewBox="0 0 22 22"><path d="M2 20L11 3l9 17z" fill="#56c8e6"/></svg></div><div class="ev-title">Hiking to Mount Elizabeth</div><div class="ev-by">by <b>Laurentie</b></div><div class="ev-meta"><b>1</b> participant(s) &nbsp;|&nbsp; <b>1</b> amis</div><div class="timeleft">time left<span>19 Hours 50 Minutes</span></div></div>
    <div class="event" style="top:584px"><div class="date">20<small>NOV</small></div><div class="ev-icon"><svg width="22" height="22" viewBox="0 0 22 22"><path d="M2 20L11 3l9 17z" fill="#56c8e6"/></svg></div><div class="ev-title">Hiking to Mount Elizabeth</div><div class="ev-by">by <b>Laurentie</b></div><div class="ev-meta"><b>1</b> participant(s) &nbsp;|&nbsp; <b>1</b> amis</div><div class="timeleft">time left<span>19 Hours 50 Minutes</span></div></div>
  </div>
</section>

<section class="abs features">
  <h2>WHAT YOU CAN DO</h2>
  <div class="feature" style="left:79px"><div class="circle"><svg width="60" height="40" viewBox="0 0 60 40"><rect x="4" y="4" width="16" height="30" rx="3" fill="#56c8e6"/><rect x="40" y="4" width="16" height="30" rx="3" fill="#56c8e6"/><path d="M20 20h20" stroke="#56c8e6" stroke-width="6"/></svg></div><h3>MEET UP</h3><p>But I must explain to you how all this mistaken idea of denouncing pleasure and praising</p></div>
  <div class="feature" style="left:349px"><div class="circle"><svg width="56" height="56" viewBox="0 0 56 56"><circle cx="28" cy="28" r="8" fill="#56c8e6"/><circle cx="10" cy="12" r="6" fill="#56c8e6"/><circle cx="46" cy="12" r="6" fill="#56c8e6"/><circle cx="28" cy="48" r="6" fill="#56c8e6"/><path d="M10 12L28 28L46 12M28 28v20" stroke="#56c8e6" stroke-width="2"/></svg></div><h3>COMMUNITY</h3><p>But I must explain to you how all this mistaken idea of denouncing pleasure and praising</p></div>
  <div class="feature" style="left:619px"><div class="circle"><svg width="56" height="40" viewBox="0 0 56 40"><circle cx="18" cy="10" r="8" fill="#56c8e6"/><circle cx="38" cy="10" r="8" fill="#56c8e6"/><path d="M2 38c0-16 32-16 32 0zM22 38c0-16 32-16 32 0z" fill="#56c8e6"/></svg></div><h3>INVITE FRIENDS</h3><p>But I must explain to you how all this mistaken idea of denouncing pleasure and praising</p></div>
  <div class="feature" style="left:889px"><div class="circle"><svg width="44" height="52" viewBox="0 0 44 52"><rect x="4" y="2" width="26" height="46" rx="4" fill="#56c8e6"/><path d="M22 30l16 8-10 4-4 8z" fill="#56c8e6" stroke="#c3da55" stroke-width="2"/></svg></div><h3>CONNECT ONLINE</h3><p>But I must explain to you how all this mistaken idea of denouncing pleasure and praising</p></div>
</section>

<footer>
  <div class="abs footer">
    <div class="col" style="left:74px"><h4>TOPICS</h4><ul><li>Popular</li><li>Trending</li></ul></div>
    <div class="col" style="left:254px"><h4>INFO</h4><ul><li>Press Releases</li><li>News</li><li>Blogs</li><li>How It Works</li></ul></div>
    <div class="col" style="left:434px"><h4>COMMUNITY</h4><ul><li>Group</li><li>Forum</li></ul></div>
    <div class="col" style="left:614px"><h4>COMPANY</h4><ul><li>About Us</li><li>Members</li><li>Register</li></ul></div>
    <div class="socials"><span><i></i>Chatterbox</span><span><i></i>Peepnest</span><span><i></i>Workweb</span><span><i></i>Pinlyst</span></div>
  </div>
  <div class="abs about-brand"><div class="brand-name">Loopsy</div></div>
  <div class="abs about"><h4>ABOUT US</h4><p>Lorem ipsum dolor sit amet, consectetur adipiscing elit, sed do eiusmod tempor incididunt ut labore et dolore magna aliqua. Ut enim ad minim veniam, quis nostrud exercitation ullamco laboris nisi ut aliquip ex ea commodo consequat. Duis aute irure dolor in reprehenderit in voluptate velit esse cillum dolore eu fugiat nulla pariatur.</p></div>
  <a class="abs ask" href="#">ASK QUESTION</a>
</footer>

</body>
</html>
```